Tick Tock Amber Kite

I'm looking for one generic business card that be used for four people or would it be easier to get four different design of cards.

I have attached the logo, of the cow. I would also like to use one colour of the cow's legs in the background.

Info for card:
Maren Holtby
Wrangler of Opportunities
Phone: 044 718 2490
email: maren.holtby@ticktockamberkites.com.au
Web: www.ticktockamberkites.com.au

Here is some tag lines that could also be used:

"Moo-ving you in the right direction"

"Putting the Tick Tock back into early childhood"
"Where's there is NO bull"

```html
<!DOCTYPE html>
<html lang="en">
<head>
<meta charset="utf-8">
<title>Tick Tock Amber Kite – Business Card</title>
<link rel="stylesheet" href="https://fonts.googleapis.com/css2?family=Lato:wght@400;700&family=Andika:wght@700&display=swap">
<style>
  :root {
    --bg: #1c1c1c;
    --card-green: #196b38;
    --card-green-light: #2c9a4e;
    --card-white: #ffffff;
    --name-lime: #8cc63e;
    --text-cream: #f3f1da;
    --brand-brown: #4a2410;
    --brand-amber: #f4a21c;
  }
  * { box-sizing: border-box; margin: 0; padding: 0; }
  html, body { width: 1200px; height: 926px; overflow: hidden; }
  body {
    background: var(--bg);
    font-family: "Lato", sans-serif;
    position: relative;
  }
  .card {
    position: absolute;
    width: 560px;
    height: 320px;
    border-radius: 3px;
    overflow: hidden;
    box-shadow: 0 12px 30px rgba(0,0,0,.55);
  }

  /* Back of card */
  .card-back {
    left: 600px;
    top: 90px;
    background: radial-gradient(ellipse at 50% 40%, var(--card-green-light) 0%, var(--card-green) 70%);
    display: flex;
    flex-direction: column;
    align-items: center;
    justify-content: center;
    text-align: center;
    color: var(--text-cream);
  }
  .tagline { font-size: 20px; line-height: 1.3; }

  /* Front of card */
  .card-front {
    left: 40px;
    top: 500px;
    background: var(--card-white);
  }
  .front-band {
    position: absolute;
    left: 0; right: 0; bottom: 0;
    height: 62%;
    background: var(--card-green);
  }
  .brand-box {
    position: absolute;
    left: 300px;
    top: 30px;
    width: 240px;
    height: 196px;
    background: var(--card-white);
    display: flex;
    flex-direction: column;
    align-items: center;
    justify-content: center;
    gap: 14px;
  }
  .brand-art {
    width: 190px;
    height: 96px;
    border-radius: 6px;
    background: linear-gradient(135deg, #6a3a1c, #4a2410);
  }
  .brand-lockup { display: flex; align-items: center; gap: 8px; }
  .brand-mark {
    width: 14px; height: 14px;
    background: var(--brand-amber);
  }
  .brand-name {
    font-family: "Andika", sans-serif;
    font-weight: 700;
    font-size: 19px;
    color: var(--brand-brown);
  }
  .person {
    position: absolute;
    left: 32px;
    top: 136px;
    color: var(--text-cream);
  }
  .person-name {
    font-size: 24px;
    font-weight: 700;
    color: var(--name-lime);
    letter-spacing: .5px;
    text-transform: uppercase;
  }
  .person-role { font-size: 13px; margin-top: 2px; }
  .contact { list-style: none; margin-top: 20px; font-size: 14.5px; line-height: 1.45; }
  .contact b { font-weight: 700; }
</style>
</head>
<body>

<section class="card card-back" aria-label="Card back">
  <p class="tagline">Moo-ving you in the right direction</p>
  <p class="tagline">Putting the Tick Tock back into early childhood</p>
  <p class="tagline">Where's there is NO bull</p>
</section>

<section class="card card-front" aria-label="Card front">
  <div class="front-band"></div>
  <div class="brand-box">
    <div class="brand-art" role="img" aria-label="Illustration of a brown cow with colourful legs"></div>
    <div class="brand-lockup">
      <span class="brand-mark"></span>
      <span class="brand-name">Tick Tock Amber Kite</span>
    </div>
  </div>
  <div class="person">
    <h1 class="person-name">Maren Holtby</h1>
    <p class="person-role">Wrangler of Opportunities</p>
    <ul class="contact">
      <li><b>phone</b>: 044 718 2490</li>
      <li><b>web</b>: www.ticktockamberkites.com.au</li>
      <li><b>email</b>: maren.holtby@ticktockamberkites.com.au</li>
    </ul>
  </div>
</section>

</body>
</html>
```